Business Card Design Project

I require a business card with the following information on them for various different people;
name
m:
f:
e:
I have a logo already and will attached that. We are in the construction industry. I require something clean and simple but eye catching at the same time. You can use another colour with our logo if you like and you can style the logo as well if you wish. I am open.
Also it needs to be front and back design.
Industry/Entity Type
Construction
Requirements
Must have
- Logo, name, mobile, fax and email address.
Front and back design

```html
<!DOCTYPE html>
<html lang="en">
<head>
<meta charset="utf-8">
<title>Stonebridge Developments — Business Cards</title>
<link rel="stylesheet" href="https://fonts.googleapis.com/css2?family=Open+Sans:wght@400;600&display=swap">
<style>
  :root {
    --backdrop: #1e1e20;
    --green-light: #9bd84a;
    --green: #6cbf2a;
    --green-deep: #4f9a1c;
    --ink: #2f3a2a;
    --ink-soft: #3c3c3c;
    --paper: #ffffff;
    --paper-shade: #eef0ee;
  }
  * { margin: 0; padding: 0; box-sizing: border-box; }
  html, body {
    width: 1200px; height: 944px; overflow: hidden;
    background: var(--backdrop);
    font-family: "Open Sans", Arial, sans-serif;
  }
  .canvas { position: relative; width: 1200px; height: 944px; }

  .card {
    position: absolute;
    width: 620px; height: 354px;
    border-radius: 26px;
    overflow: hidden;
  }

  /* Front */
  .card-front {
    left: 90px; top: 90px;
    background: radial-gradient(ellipse at 60% 35%, var(--green-light) 0%, var(--green) 55%, var(--green-deep) 100%);
  }
  .brand {
    position: absolute; left: 0; right: 0; top: 120px;
    display: flex; align-items: center; justify-content: center; gap: 18px;
  }
  .brand-square {
    width: 44px; height: 44px; background: var(--ink);
  }
  .brand-name {
    color: var(--ink); font-weight: 400; font-size: 40px; letter-spacing: 0.5px;
  }
  .front-web {
    position: absolute; left: 0; right: 0; top: 240px;
    text-align: center; color: var(--paper);
    font-size: 19px; letter-spacing: 2px;
  }

  /* Back */
  .card-back {
    left: 490px; top: 500px;
    background: linear-gradient(180deg, var(--paper) 0%, var(--paper) 70%, var(--paper-shade) 100%);
  }
  .side-band {
    position: absolute; top: 0; bottom: 0; left: 34px; width: 30px;
    background: linear-gradient(90deg, var(--green-deep), var(--green));
  }
  .side-rule {
    position: absolute; top: 0; bottom: 0; left: 72px; width: 4px;
    background: var(--green);
  }
  .person { position: absolute; left: 120px; top: 60px; }
  .person-name { font-size: 23px; color: var(--ink-soft); font-weight: 400; }
  .person-role { font-size: 15px; color: var(--green); margin-top: -2px; }

  .contacts {
    position: absolute; left: 120px; top: 206px;
    list-style: none; font-size: 17px; color: var(--ink-soft); line-height: 23px;
  }
  .contacts li { display: flex; align-items: center; gap: 10px; }
  .contacts svg { width: 14px; height: 14px; flex: none; }
  .contacts .web-accent { color: var(--green-deep); }

  .back-mark {
    position: absolute; right: 54px; bottom: 50px;
    width: 96px; height: 96px;
    background: linear-gradient(180deg, var(--green-light), var(--green-deep));
  }
</style>
</head>
<body>
<main class="canvas">

  <section class="card card-front" aria-label="Card front">
    <div class="brand">
      <span class="brand-square"></span>
      <span class="brand-name">Stonebridge Developments</span>
    </div>
    <p class="front-web">www.stonebridgeworks.com</p>
  </section>

  <section class="card card-back" aria-label="Card back">
    <div class="side-band"></div>
    <div class="side-rule"></div>

    <div class="person">
      <h1 class="person-name">Mark Ellery</h1>
      <p class="person-role">director</p>
    </div>

    <ul class="contacts">
      <li>
        <svg viewBox="0 0 14 14" aria-hidden="true"><path d="M3 1 L5.5 1 L6.5 4 L5 5.2 Q6.3 8 8.8 9 L10 7.5 L13 8.5 L13 11 Q12 13 10 13 Q2 12 1 4 Q1 2 3 1 Z" fill="#6cbf2a"/></svg>
        <span>555-014-2200</span>
      </li>
      <li>
        <svg viewBox="0 0 14 14" aria-hidden="true"><rect x="1" y="5" width="12" height="7" rx="1" fill="#6cbf2a"/><rect x="4" y="1" width="6" height="5" fill="#6cbf2a"/><rect x="3.5" y="8" width="7" height="1.5" fill="#fff"/></svg>
        <span>555-014-2201</span>
      </li>
      <li>
        <svg viewBox="0 0 14 14" aria-hidden="true"><rect x="1" y="3" width="12" height="8" rx="1" fill="#6cbf2a"/><path d="M1.5 3.5 L7 8 L12.5 3.5" stroke="#fff" stroke-width="1.2" fill="none"/></svg>
        <span>info@stonebridgeworks.com</span>
      </li>
      <li>
        <svg viewBox="0 0 14 14" aria-hidden="true"><circle cx="7" cy="7" r="6" fill="#6cbf2a"/></svg>
        <span>www.<span class="web-accent">stonebridgeworks</span>.com</span>
      </li>
    </ul>

    <div class="back-mark" aria-hidden="true"></div>
  </section>

</main>
</body>
</html>
```